Double caffeinated coffee label design

We need to design labels for a new coffee brand. The label size: 2.75” x 4.125” (Corners slightly rounded). There will be front and back label in stickers to be put on standardized bags. Our product is roasted whole bean and ground coffee in 12oz bags. It is described as "strong, bold, intense, and double caffeinated. The product is designed for passionate coffee drinkers who want strong, more caffeinated but not bitter coffee. The coffee is suitable for espresso base coffees.
Target Market(s)
Groceries, food stores, super markets. Heavy and sophisticated coffee drinkers.
Requirements
Must have
- Modern, minimalist style. Strong and bold look. Creative. Impressive.
Nice to have
- Some impressed coffee label designs for reference: https://www.trevalo.net/find?q=most+impressive+coffee+brand+designs&from=qwer&kind=pics&sa=Y&ref=7bZkQxmPtLrsWvNcYhDjKeFgAoUiBnMwZpRsTeQvLbXy_KHJaPqWz&vw=1280&vh=610#pic=kR4mTzWqPxNbLo:

```html
<!DOCTYPE html>
<html lang="en">
<head>
<meta charset="utf-8">
<title>Kordo Coffee – Double Caffeinated Label</title>
<link rel="stylesheet" href="https://fonts.googleapis.com/css2?family=Quicksand:wght@400;500;600&display=swap">
<style>
  :root {
    --backdrop: #cbc6bb;
    --label-black: #0e0e0e;
    --ink-light: #dcdcdc;
    --ink-soft: #bdbdbd;
    --accent-orange: #c9522a;
  }
  * { margin: 0; padding: 0; box-sizing: border-box; }
  html, body {
    width: 1122px;
    height: 1200px;
    overflow: hidden;
    background: var(--backdrop);
  }
  body {
    font-family: "Quicksand", "Helvetica Neue", Arial, sans-serif;
    color: var(--ink-light);
  }
  .label {
    position: absolute;
    left: 201px;
    top: 60px;
    width: 720px;
    height: 1080px;
    background: var(--label-black);
    border-radius: 28px;
  }
  .tagline {
    position: absolute;
    top: 96px;
    width: 100%;
    text-align: center;
    font-size: 40px;
    font-weight: 500;
    letter-spacing: 2px;
  }
  .tagline .divider {
    display: inline-block;
    width: 3px;
    height: 40px;
    margin: 0 12px;
    background: var(--accent-orange);
    vertical-align: -6px;
  }
  .brand {
    position: absolute;
    top: 290px;
    width: 100%;
    text-align: center;
    color: var(--ink-soft);
    font-weight: 500;
  }
  .brand-name {
    display: block;
    font-size: 112px;
    line-height: 1;
    letter-spacing: 2px;
  }
  .brand-descriptor {
    display: block;
    margin-top: 8px;
    font-size: 34px;
    letter-spacing: 6px;
    padding-left: 90px;
  }
  .rule {
    position: absolute;
    top: 494px;
    left: 145px;
    width: 470px;
    height: 3px;
    background: var(--accent-orange);
  }
  .product-claim {
    position: absolute;
    top: 526px;
    width: 100%;
    text-align: center;
    font-size: 30px;
    font-weight: 600;
    letter-spacing: 2px;
  }
  .format-badge {
    position: absolute;
    top: 612px;
    left: 230px;
    width: 260px;
    height: 260px;
  }
  .format-badge text {
    font-family: "Quicksand", "Helvetica Neue", Arial, sans-serif;
    font-size: 21px;
    font-weight: 500;
    letter-spacing: 3px;
    fill: var(--ink-light);
  }
  .footer-line {
    position: absolute;
    top: 942px;
    left: 84px;
    font-size: 20px;
    font-weight: 500;
    letter-spacing: 1px;
  }
  .footer-line .net-weight {
    font-size: 28px;
    font-weight: 600;
    margin-right: 18px;
  }
</style>
</head>
<body>
  <main class="label">
    <p class="tagline">strong<span class="divider"></span>bold<span class="divider"></span>intense</p>

    <h1 class="brand">
      <span class="brand-name">Kordo</span>
      <span class="brand-descriptor">COFFEE</span>
    </h1>

    <div class="rule"></div>

    <p class="product-claim">DOUBLE&nbsp;&nbsp;CAFFEEINATED</p>

    <svg class="format-badge" viewBox="0 0 260 260" aria-label="Roasted whole bean, ground coffee">
      <defs>
        <path id="badge-top-arc" d="M 42 130 A 88 88 0 0 1 218 130"/>
        <path id="badge-bottom-arc" d="M 30 130 A 100 100 0 0 0 230 130"/>
      </defs>
      <path d="M 34 140 A 96 96 0 0 1 226 140" fill="none" stroke="var(--accent-orange)" stroke-width="2"/>
      <text><textPath href="#badge-top-arc" startOffset="50%" text-anchor="middle">ROASTED WHOLE BEAN</textPath></text>
      <text><textPath href="#badge-bottom-arc" startOffset="50%" text-anchor="middle" dominant-baseline="hanging">GROUND COFFEE</textPath></text>
      <line x1="88" y1="132" x2="172" y2="132" stroke="var(--accent-orange)" stroke-width="3"/>
    </svg>

    <p class="footer-line"><span class="net-weight">12oz</span>suitable for espresso base coffees</p>
  </main>
</body>
</html>
```